Power point template for corporate use

We need a simple power point template to use with our new logo design for corporate presentations to prospects

Target Market(s)

Corporate marketing departments - clients purchase our services and data

```html
<!DOCTYPE html>
<html lang="en">
<head>
<meta charset="utf-8">
<title>Lumo Digital – Presentation Template</title>
<link rel="stylesheet" href="https://fonts.googleapis.com/css2?family=PT+Sans:wght@400;700&display=swap">
<style>
  :root {
    --stage-light: #a9aaac;
    --stage-dark: #7c7d80;
    --pink-bright: #ff2f8e;
    --pink-deep: #c21c6b;
    --pink-ring: #c8196f;
    --slate: #5a5a5c;
    --rule: #9c9c9e;
    --white: #ffffff;
    --brand-red: #d8313a;
  }
  * { margin: 0; padding: 0; box-sizing: border-box; }
  html, body { width: 1200px; height: 1000px; overflow: hidden; }
  body {
    position: relative;
    background: radial-gradient(ellipse 700px 520px at 600px 480px, var(--stage-light), var(--stage-dark));
    font-family: "PT Sans", "Myriad Pro", sans-serif;
  }
  .slide { position: absolute; overflow: hidden; }
  .slide svg { position: absolute; inset: 0; display: block; }
  .slide--cover { left: 31px; top: 301px; width: 562px; height: 397px; }
  .slide--content { left: 612px; top: 301px; width: 561px; height: 395px; background: var(--slate); }

  .cover-title {
    position: absolute; left: 35px; top: 36px;
    font-size: 46px; font-weight: 400; color: var(--white); line-height: 1;
  }
  .cover-title-reflection {
    position: absolute; left: 35px; top: 83px;
    font-size: 46px; color: var(--white); line-height: 1;
    transform: scaleY(-1);
    opacity: 0.55;
    -webkit-mask-image: linear-gradient(to top, rgba(0,0,0,0.9), transparent 55%);
    mask-image: linear-gradient(to top, rgba(0,0,0,0.9), transparent 55%);
  }
  .brand-mark {
    position: absolute; left: 78px; top: 252px;
    font-size: 38px; font-weight: 700; color: var(--brand-red);
    letter-spacing: 1px; line-height: 1;
  }

  .content-header {
    position: absolute; left: 0; top: 0; width: 561px; height: 68px;
  }
  .content-title {
    position: absolute; left: 28px; top: 12px;
    font-size: 44px; color: var(--white); line-height: 1;
  }
  .content-list {
    position: absolute; left: 42px; top: 110px;
    list-style: none; color: var(--white); font-size: 20px;
  }
  .content-list li { position: relative; padding-left: 18px; }
  .content-list li::before {
    content: ""; position: absolute; left: 0; top: 8px;
    width: 10px; height: 10px; border-radius: 50%; background: var(--white);
  }
  .brand-mark--small {
    position: absolute; right: 24px; bottom: 8px;
    font-size: 13px; font-weight: 700; color: var(--white); letter-spacing: 0.5px;
  }
</style>
</head>
<body>

<section class="slide slide--cover">
  <svg viewBox="0 0 562 397" width="562" height="397" aria-hidden="true">
    <defs>
      <linearGradient id="coverPink" x1="0" y1="0" x2="1" y2="0">
        <stop offset="0" stop-color="var(--pink-bright)"/>
        <stop offset="1" stop-color="var(--pink-deep)"/>
      </linearGradient>
      <linearGradient id="coverGloss" x1="0" y1="0" x2="1" y2="1">
        <stop offset="0" stop-color="#ffffff" stop-opacity="0.6"/>
        <stop offset="0.6" stop-color="#ffffff" stop-opacity="0.08"/>
        <stop offset="1" stop-color="#ffffff" stop-opacity="0"/>
      </linearGradient>
    </defs>
    <rect width="562" height="397" fill="url(#coverPink)"/>
    <circle cx="545" cy="262" r="258" fill="url(#coverGloss)"/>
    <ellipse cx="172" cy="322" rx="227" ry="193" fill="var(--white)"/>
    <ellipse cx="172" cy="322" rx="220" ry="186" fill="var(--pink-ring)"/>
    <ellipse cx="167" cy="326" rx="213" ry="178" fill="var(--white)"/>
  </svg>
  <h1 class="cover-title">Title Here</h1>
  <div class="cover-title-reflection" aria-hidden="true">Title Here</div>
  <div class="brand-mark">LUMO DIGITAL</div>
</section>

<section class="slide slide--content">
  <svg class="content-header" viewBox="0 0 561 68" width="561" height="68" aria-hidden="true">
    <defs>
      <linearGradient id="headerPink" x1="0" y1="0" x2="1" y2="0">
        <stop offset="0" stop-color="var(--pink-bright)"/>
        <stop offset="1" stop-color="var(--pink-deep)"/>
      </linearGradient>
      <linearGradient id="headerGloss" x1="0" y1="0" x2="1" y2="1">
        <stop offset="0" stop-color="#ffffff" stop-opacity="0.55"/>
        <stop offset="1" stop-color="#ffffff" stop-opacity="0.05"/>
      </linearGradient>
    </defs>
    <rect width="561" height="66" fill="url(#headerPink)"/>
    <circle cx="520" cy="230" r="185" fill="url(#headerGloss)"/>
    <rect y="66" width="561" height="2" fill="var(--rule)"/>
  </svg>
  <h2 class="content-title">Title Here</h2>
  <ul class="content-list">
    <li>Content Here</li>
  </ul>
  <div class="brand-mark--small">LUMO DIGITAL</div>
</section>

</body>
</html>
```